Flyer for home based dog grooming salon

I need a flyer design for my home based dog grooming business. This flyer will be used for letterbox drops and supplied to local businesses such as vets. I may also extend the design at a later date for business cards as well.
Key advantages I want highlighted are listed below. They are listed in order of importance so that if the flyer becomes too busy, the less important items can be left off:
- "one on one personalised service where the groomer listens to your needs"
- NO CAGING...pets groomed immediately
- the same groomer for your pet at each groom, making your pet more comfortable
- local business in Linden Vale
- modern, air-conditioned salon
- VIP program offering discounts for regular clients
List of services to be included are listed below:
- tidy-ups
- full-body clipping
- strip-outs
- breed specific clips
- and more...
Phone number, website and email address all need to be indicated clearly so they stand out
0472 518 264 (use the spacing as shown)
www.tallowridgetrims.com.au
info@tallowridgetrims.com.au
I have no strong preferences for colours, however, as I am a male groomer, I don't want the flyer to be too feminine but also not too masculine as many of the prospective customers are female.
I have seen good examples of flyers with images of dogs being groomed on them and flyers with just images of dogs on them and I have no preference for either - it will depend on the overall look of the flyer. If you wish to include images of dogs being groomed, I have uploaded 38 images of dogs being groomed taken from my salon. I don't want images of anyone else grooming dogs on the flyer. As i cater to all size dogs, any images of dogs do not need to limited to small breeds.
The flyer size will be DL (99 x 210 mm) and can be single or double sided. If you plan on doing double sided, please ensure the list of services offered is shown on the front side.
As an example of several designs I have seen before, in 2012 there was a project for Pemberly Pawcare. From designs submitted, I liked #1135917, #1137543, #1135911 and probably would have gone for #1140593. I did not like the winner.
Dog owners
Salon

```html
<!DOCTYPE html>
<html lang="en">
<head>
<meta charset="utf-8">
<title>Home Based Dog Grooming Flyer</title>
<link rel="stylesheet" href="https://fonts.googleapis.com/css2?family=Questrial&family=Lato:ital,wght@0,400;0,700;1,900&family=Arimo:wght@400;700&display=swap">
<style>
  :root {
    --page-bg: #e9e6e1;
    --flyer-dark: #161616;
    --flyer-dark-2: #262626;
    --brand-red: #b3141b;
    --brand-red-dark: #8c0f14;
    --white: #ffffff;
    --ink: #111111;
    --box-grey: #d9d9d9;
    --photo-warm: #c9b9a4;
    --photo-cool: #8e8a86;
  }
  * { margin: 0; padding: 0; box-sizing: border-box; }
  html, body { width: 904px; height: 1200px; overflow: hidden; }
  body { background: var(--page-bg); position: relative; }

  .flyer {
    position: absolute; left: 190px; top: 46px; width: 524px; height: 1108px;
    background: linear-gradient(180deg, var(--flyer-dark-2) 0%, var(--flyer-dark) 45%, var(--flyer-dark-2) 100%);
    overflow: hidden;
    font-family: "Lato", sans-serif;
  }

  .headline { position: absolute; left: 0; top: 14px; width: 100%; text-align: center; font-family: "Questrial", sans-serif; line-height: 1; }
  .headline-top { color: var(--white); font-size: 46px; letter-spacing: 0.5px; }
  .headline-main { color: var(--brand-red); font-size: 47px; margin-top: 6px; letter-spacing: 0.5px; }

  .hero-art { position: absolute; left: 0; top: 0; width: 524px; height: 540px; }

  .services-box {
    position: absolute; left: 54px; top: 506px; width: 190px; height: 192px;
    background: linear-gradient(180deg, var(--white) 0%, var(--white) 55%, var(--box-grey) 100%);
    border-radius: 10px; text-align: center; padding-top: 10px;
    font-family: "Arimo", sans-serif;
  }
  .services-title { color: var(--brand-red); font-size: 31px; font-weight: 700; letter-spacing: 0.3px; }
  .services-list { list-style: none; margin-top: 4px; }
  .services-list li { font-size: 16.5px; color: var(--ink); line-height: 26px; white-space: nowrap; }
  .services-list svg { width: 12px; height: 12px; vertical-align: 0; margin-right: 3px; }

  .detail-photo { position: absolute; left: 291px; top: 502px; width: 210px; height: 210px; }

  .promise {
    position: absolute; left: 20px; top: 724px; width: 500px;
    color: var(--brand-red); font-weight: 900; font-style: italic; font-size: 24.5px; line-height: 31px;
    text-shadow: 1px 1px 0 var(--brand-red-dark);
  }

  .benefits { position: absolute; left: 20px; top: 808px; list-style: none; }
  .benefits li { position: relative; padding-left: 22px; color: var(--white); font-weight: 700; font-size: 18.5px; line-height: 26px; }
  .benefits li::before {
    content: ""; position: absolute; left: 2px; top: 8px; width: 0; height: 0;
    border-left: 11px solid var(--brand-red); border-top: 5px solid transparent; border-bottom: 5px solid transparent;
  }

  .contact {
    position: absolute; left: 0; bottom: 0; width: 100%; height: 114px; background: var(--white);
    text-align: center; padding-top: 12px; color: var(--ink); font-family: "Lato", sans-serif; font-weight: 700;
  }
  .contact-line { display: flex; align-items: center; justify-content: center; gap: 8px; line-height: 31px; }
  .contact-phone { font-size: 25px; }
  .contact-web, .contact-email { font-size: 23px; font-weight: 400; color: var(--ink); }
  .contact-line svg { flex: none; }
</style>
</head>
<body>
<main class="flyer">
  <svg class="hero-art" viewBox="0 0 524 540" aria-hidden="false">
    <defs>
      <linearGradient id="salonPhotoTone" x1="0" y1="0" x2="1" y2="1">
        <stop offset="0" stop-color="#d8d6d2"/>
        <stop offset="0.5" stop-color="#a7a19a"/>
        <stop offset="1" stop-color="#e4ddd2"/>
      </linearGradient>
    </defs>
    <path d="M0,200 C160,120 360,95 524,160 L524,220 C380,170 200,180 0,232 Z" fill="var(--brand-red)"/>
    <path d="M0,225 C190,178 360,168 524,212 L524,445 C400,478 250,500 0,452 Z" fill="url(#salonPhotoTone)" role="img" aria-label="Photo of the groomer in his salon beside a freshly clipped white standard poodle"/>
    <path d="M0,448 C250,498 400,474 524,440 L524,478 C400,508 250,528 0,492 Z" fill="var(--white)"/>
    <path d="M0,490 C250,526 400,506 524,476 L524,488 C400,520 250,542 0,504 Z" fill="var(--brand-red)"/>
  </svg>

  <header class="headline">
    <h1 class="headline-top">Home based</h1>
    <h2 class="headline-main">DOG GROOMING</h2>
  </header>

  <section class="services-box">
    <h3 class="services-title">SERVICES</h3>
    <ul class="services-list">
      <li><svg viewBox="0 0 12 12"><g fill="var(--brand-red)"><ellipse cx="6" cy="8.3" rx="3" ry="2.5"/><circle cx="2" cy="5" r="1.3"/><circle cx="4.5" cy="2.6" r="1.3"/><circle cx="7.5" cy="2.6" r="1.3"/><circle cx="10" cy="5" r="1.3"/></g></svg>Tidy-ups</li>
      <li><svg viewBox="0 0 12 12"><g fill="var(--brand-red)"><ellipse cx="6" cy="8.3" rx="3" ry="2.5"/><circle cx="2" cy="5" r="1.3"/><circle cx="4.5" cy="2.6" r="1.3"/><circle cx="7.5" cy="2.6" r="1.3"/><circle cx="10" cy="5" r="1.3"/></g></svg>Full-body clipping</li>
      <li><svg viewBox="0 0 12 12"><g fill="var(--brand-red)"><ellipse cx="6" cy="8.3" rx="3" ry="2.5"/><circle cx="2" cy="5" r="1.3"/><circle cx="4.5" cy="2.6" r="1.3"/><circle cx="7.5" cy="2.6" r="1.3"/><circle cx="10" cy="5" r="1.3"/></g></svg>Strip-outs</li>
      <li><svg viewBox="0 0 12 12"><g fill="var(--brand-red)"><ellipse cx="6" cy="8.3" rx="3" ry="2.5"/><circle cx="2" cy="5" r="1.3"/><circle cx="4.5" cy="2.6" r="1.3"/><circle cx="7.5" cy="2.6" r="1.3"/><circle cx="10" cy="5" r="1.3"/></g></svg>Breed specific clips</li>
      <li><svg viewBox="0 0 12 12"><g fill="var(--brand-red)"><ellipse cx="6" cy="8.3" rx="3" ry="2.5"/><circle cx="2" cy="5" r="1.3"/><circle cx="4.5" cy="2.6" r="1.3"/><circle cx="7.5" cy="2.6" r="1.3"/><circle cx="10" cy="5" r="1.3"/></g></svg>and more...</li>
    </ul>
  </section>

  <svg class="detail-photo" viewBox="0 0 210 210">
    <defs>
      <radialGradient id="combPhotoTone" cx="0.45" cy="0.45" r="0.6">
        <stop offset="0" stop-color="#cfc7bd"/>
        <stop offset="1" stop-color="#7d756d"/>
      </radialGradient>
    </defs>
    <circle cx="105" cy="105" r="104" fill="var(--white)"/>
    <circle cx="105" cy="105" r="95" fill="url(#combPhotoTone)" role="img" aria-label="Close-up photo of a curly-coated dog being combed around the eye"/>
  </svg>

  <p class="promise">"one on one personalised service where the groomer listens to your needs"</p>

  <ul class="benefits">
    <li>NO CAGING...pets groomed immediately</li>
    <li>the same groomer for your pet at each groom,<br>making your pet more comfortable</li>
    <li>local business in Linden Vale</li>
    <li>modern, air-conditioned salon</li>
    <li>VIP program offering discounts for regular clients</li>
  </ul>

  <footer class="contact">
    <div class="contact-line contact-phone">
      <svg width="18" height="18" viewBox="0 0 18 18"><rect width="18" height="18" rx="3" fill="var(--brand-red)"/><path d="M5.2,3.8 L7.4,3.6 L8.2,6.6 L6.9,7.6 C7.6,9.2 8.8,10.4 10.4,11.1 L11.4,9.8 L14.4,10.6 L14.2,12.8 C9.2,13.6 4.4,8.8 5.2,3.8 Z" fill="var(--white)"/></svg>
      <span>0472 518 264</span>
    </div>
    <div class="contact-line contact-web">
      <svg width="20" height="20" viewBox="0 0 20 20" fill="none" stroke="var(--brand-red)" stroke-width="1.6"><circle cx="10" cy="10" r="8"/><ellipse cx="10" cy="10" rx="3.5" ry="8"/><path d="M2,10 H18 M3.5,5.5 H16.5 M3.5,14.5 H16.5"/></svg>
      <span>www.tallowridgetrims.com.au</span>
    </div>
    <div class="contact-line contact-email">
      <svg width="22" height="14" viewBox="0 0 22 14"><rect width="22" height="14" fill="var(--brand-red)"/><path d="M1,1 L11,8 L21,1" fill="none" stroke="var(--white)" stroke-width="1.6"/></svg>
      <span>info@tallowridgetrims.com.au</span>
    </div>
  </footer>
</main>
</body>
</html>
```